Illustrate a statistic and its significance

Please create a graphical representation of the success rate of the Vail Procedure for our website. The Vail Procedure has a success rate of 80%. This means the procedure is successful for 8 out of every 10 people. An 80% success rate by itself is great. However, it's even more impressive when you consider that the only people we perform this procedure on are patients who have exhausted conventional treatment options for migraines and headaches. I would really like to emphasize both the success rate and the type of patients we are successful in treating with this procedure.
For example, you could create an illustration of outlines of 10 people with 8 of them shaded in, which would represent an 80% success rate. Then, underneath this image, you could add a bullet list of the types of treatments patients (such as the 10 figures in the image) have tried before coming to us/having this procedure, which include the following:
Prescription medications
Trigger point injections
Nerve blocks
Migraine surgery
Dermil
Chiropractic care
Physical therapy
Biofeedback
Massage
Acupuncture
Or maybe there is another/better way to represent this statistic graphically? I'm just looking for an effective illustration of this important statistic and its significance.
Our brand colors are red (#fd444a) and blue (#214170)
Thank you!
People who suffer from chronic migraines and headaches
Healthcare/Medical
- Athiti

```html
<!DOCTYPE html>
<html lang="en">
<head>
<meta charset="utf-8">
<title>Vail Procedure – Success Rate</title>
<link rel="stylesheet" href="https://fonts.googleapis.com/css2?family=Encode+Sans+Expanded:wght@400;500;600;700;800&display=swap">
<style>
  :root{
    --brand-blue:#1f3f6e;
    --brand-red:#e8474f;
    --figure-muted:#c9c8d6;
    --canvas-bg:#efefef;
    --card-bg:#eeeeee;
    --ink:#1d1d1f;
    --white:#ffffff;
  }
  *{margin:0;padding:0;box-sizing:border-box}
  html,body{width:1200px;height:691px;overflow:hidden;background:var(--canvas-bg)}
  body{font-family:"Encode Sans Expanded",sans-serif;color:var(--ink)}
  .poster{position:relative;width:1200px;height:691px;overflow:hidden;background:var(--canvas-bg)}

  .portrait{
    position:absolute;left:545px;top:50px;width:655px;height:641px;
    background:radial-gradient(ellipse at 62% 40%, #9a9a9a 0%, #c4c4c4 35%, #dcdcdc 60%, rgba(239,239,239,0) 78%);
  }

  .headline{
    position:absolute;left:53px;top:70px;
    font-size:33px;line-height:54px;font-weight:600;color:var(--brand-blue);letter-spacing:.6px;
  }
  .headline .accent{color:var(--brand-red);font-weight:700}

  .stat-backdrop{
    position:absolute;left:278px;top:297px;width:344px;height:156px;
    background:var(--brand-red);border-top-right-radius:38px;
  }
  .stat-card{
    position:absolute;left:52px;top:214px;width:528px;height:206px;
    background:var(--card-bg);border-top-right-radius:52px;
    box-shadow:0 2px 10px rgba(0,0,0,.28);
  }
  .figures{position:absolute;left:17px;top:27px;width:220px;height:164px}
  .stat-copy{
    position:absolute;left:247px;top:29px;
    font-size:24px;line-height:32.5px;font-weight:400;color:var(--brand-blue);letter-spacing:.4px;
  }
  .stat-copy strong{font-weight:800}
  .rate-badge{
    position:absolute;left:402px;top:136px;width:126px;height:51px;
    background:var(--brand-red);color:var(--white);
    display:flex;align-items:center;
  }
  .rate-value{font-size:36px;font-weight:500;margin-left:10px;letter-spacing:.5px}
  .rate-label{
    font-size:7.5px;line-height:8px;font-weight:600;
    writing-mode:vertical-rl;transform:rotate(180deg);margin-left:4px;text-align:center;
  }

  .services-title{
    position:absolute;left:53px;top:486px;height:30px;
    border-left:6px solid var(--brand-red);padding-left:8px;
    font-size:28px;line-height:30px;font-weight:500;color:var(--brand-red);letter-spacing:.5px;
  }
  .services-title b{font-weight:700}
  .service-list{
    position:absolute;top:524px;list-style:none;
    font-size:18.5px;line-height:25px;font-weight:400;color:var(--ink);letter-spacing:.6px;
  }
  .service-list li::before{content:"•";margin-right:8px}
  .service-list.col-a{left:56px}
  .service-list.col-b{left:321px}
</style>
</head>
<body>
<main class="poster">
  <div class="portrait" role="img" aria-label="Black and white photo of a woman holding her temples in pain, red glow marking the headache"></div>

  <h1 class="headline">Exhausted with conventional treatment<br>for <span class="accent">Migraines and Headaches?</span></h1>

  <div class="stat-backdrop"></div>
  <section class="stat-card">
    <svg class="figures" viewBox="0 0 220 164" aria-label="8 of 10 people figures highlighted">
      <defs>
        <g id="person">
          <circle cx="17.5" cy="8" r="8"/>
          <path d="M4 19 H31 Q35 19 35 23 V45 Q35 48 32 48 V37 H30 V73 Q30 77 26 77 H21 Q19 77 19 74 V52 H16 V74 Q16 77 14 77 H9 Q5 77 5 73 V37 H3 V48 Q0 48 0 45 V23 Q0 19 4 19 Z"/>
        </g>
      </defs>
      <g fill="var(--brand-blue)">
        <use href="#person" x="0" y="0"/>
        <use href="#person" x="45" y="0"/>
        <use href="#person" x="91" y="0"/>
        <use href="#person" x="136" y="0"/>
        <use href="#person" x="181" y="0"/>
        <use href="#person" x="0" y="86"/>
        <use href="#person" x="45" y="86"/>
        <use href="#person" x="91" y="86"/>
      </g>
      <g fill="var(--figure-muted)">
        <use href="#person" x="136" y="86"/>
        <use href="#person" x="181" y="86"/>
      </g>
    </svg>
    <p class="stat-copy">We offer a successful<br>procedure of <strong>8 out<br>of 10 people</strong></p>
    <div class="rate-badge">
      <span class="rate-value">80%</span>
      <span class="rate-label">Success<br>Rate</span>
    </div>
  </section>

  <h2 class="services-title">Our <b>Services</b></h2>
  <ul class="service-list col-a">
    <li>Prescription medications</li>
    <li>Trigger point injections</li>
    <li>Nerve blocks</li>
    <li>Migraine surgery</li>
    <li>Dermil</li>
  </ul>
  <ul class="service-list col-b">
    <li>Chiropractic care</li>
    <li>Physical therapy</li>
    <li>Biofeedback</li>
    <li>Massage</li>
    <li>Acupuncture</li>
  </ul>
</main>
</body>
</html>
```